Quillmont Booking Engine Marketing Site

Hi,
I’m currently in the process of putting together a web application with the intention of providing small resorts/B&Bs/small hotels the ability to allow their customers to book online.
I’m looking to have a design created for a marketing site, to give potential customers additional information about my booking engine, as well as to help drive sign-ups. A lot of the competition out there appears outdated, so I would like something that is more modern and up to date.
I am looking for just the design (i’m a web developer, but I lack the creative skills for a good marketing site)
For some more background, I will be targeting business owners of smaller resorts and Bed & Breakfasts. These are typically family owned small businesses that may only have a 10 room setup. These businesses will also typically have additional amenities that they will have to rent out or sell to their clients ( ex. Spa, fruit basket, water sport rentals). My software will provide them with the ability to sell their amenities as well.
I’m open to different designs, but my main thing is I want it to look modern, and I want it to have several callouts to sign up for my product.
I am looking to have the homepage created, 1 interior page, and a style guide created (to show form fields, H1’s, etc.).
I had a logo created a couple months ago that will be included with this project brief.
If you need any additional information feel free to reach out to me.

Target Market(s)

This site will be targeted small business owners who are running small resorts, Bed and Breakfasts, or any business that provides rooms for their clients.

Industry/Entity Type

Saas

Number of Pages Required

2 page

Font styles to use
Sans Serif

Colors

Designer to choose colors to be used in the design.

Requirements
Must have
• A modern feel, with several CTA's that will drive to the registration page on the homepage. on the internal page, I mostly just need the page layout, I will reuse that page layout. and a style guide if at all possible (include colors, form fields, H1's, etc.)
Nice to have
• maybe a hero image at the top with buttons over the top? again i'm pretty open to most anything.
Should not have
• I like images, but I don't want the page overrun with images. A good balance.

```html
<!DOCTYPE html>
<html lang="en">
<head>
<meta charset="utf-8">
<title>Quillmont Booking Engine</title>
<link rel="stylesheet" href="https://fonts.googleapis.com/css2?family=Open+Sans:ital,wght@0,300;0,400;0,600;0,700;1,300;1,400&family=Roboto:wght@300;400&display=swap">
<style>
:root{
  --navy:#004b82;
  --green:#7ab800;
  --white:#ffffff;
  --ink:#2b2b2b;
  --grey:#555555;
  --rule:#d6d6d6;
  --footer:#f0f1f0;
  --dot:#c8c8c8;
}
*{box-sizing:border-box;margin:0;padding:0}
html,body{width:1200px;height:2850px;overflow:hidden}
body{font-family:"Open Sans",Arial,sans-serif;color:var(--ink);background:var(--white);position:relative}
section,header,footer,.topbar{position:absolute;left:0;width:1200px}
.abs{position:absolute}
svg{display:block}

/* top bar */
.topbar{top:0;height:50px;background:var(--navy);color:var(--white)}
.topbar .social{left:770px;top:15px;display:flex;gap:10px;align-items:center}
.dot-icon{width:16px;height:16px;border-radius:50%;background:currentColor;display:block}
.topbar .account{top:12px;font-size:18px;font-weight:600}

/* header */
.site-header{top:50px;height:111px}
.brand{display:flex;align-items:center;gap:12px;color:var(--navy);font-weight:600;line-height:1}
.brand .mark{border-radius:50%;background:var(--green);flex:none}
.brand .name{font-size:40px;letter-spacing:1px}
.brand .tag{font-size:25px;letter-spacing:1px;margin-top:4px}
.site-header .brand{left:38px;top:20px}
.site-header .brand .mark{width:66px;height:66px}
.main-nav{right:46px;top:48px;display:flex;gap:27px;font-size:17px;font-weight:700;letter-spacing:-.5px;text-transform:uppercase;color:var(--ink)}
.main-nav .current{position:relative}
.main-nav .current::after{content:"";position:absolute;left:0;right:0;bottom:-9px;height:4px;background:var(--navy)}

/* hero */
.hero{top:161px;height:512px;background:linear-gradient(120deg,#5d5a57 0%,#8d8780 35%,#b9b0a6 55%,#7f6e60 80%,#5a4a3f 100%)}
.hero::before{content:"";position:absolute;inset:0;background:rgba(40,40,40,.35)}
.hero .rule{left:246px;width:708px;height:2px;background:rgba(255,255,255,.85)}
.hero .intro{left:246px;top:150px;width:708px;color:var(--white);font-size:18px;font-weight:600;line-height:23px}
.btn-outline{border:2px solid var(--white);color:var(--white);display:flex;align-items:center;justify-content:center}
.hero .btn-outline{left:508px;top:365px;width:182px;height:58px;font-size:22px;font-weight:600}

/* feature tiles */
.features{top:673px;height:180px;display:flex}
.tile{width:300px;height:180px;position:relative;color:var(--white);text-align:center}
.tile:nth-child(4){width:300px;flex:1}
.tile.navy{background:var(--navy)}
.tile.green{background:var(--green)}
.tile svg{position:absolute;left:50%;top:34px;transform:translateX(-50%)}
.tile h3{position:absolute;top:114px;width:100%;font-size:17px;font-weight:600}
.tile p{position:absolute;top:140px;width:100%;font-size:10px;font-style:italic}

/* shared section headings */
.section-title{font-size:36px;font-weight:700;text-align:center;width:500px;left:76px;line-height:1}
.lede{left:76px;width:500px;text-align:center;font-size:17px;font-style:italic;font-weight:300;color:var(--grey);line-height:26px}
.accent{height:7px;background:var(--navy)}
.divider{left:52px;width:1096px;height:1px;background:var(--rule)}

/* rooms */
.rooms{top:853px;height:456px}
.arrow-btn{width:46px;height:50px;background:var(--navy);display:flex;align-items:center;justify-content:center}
.room-card{left:762px;top:94px;width:301px;height:266px;border:3px solid var(--navy);padding:10px}
.room-photo{width:100%;height:100%;background:linear-gradient(160deg,#7a5a3f 0%,#b98a5e 40%,#d9cdbf 60%,#e0621e 80%,#c84f14 100%)}
.room-name{left:773px;top:364px;font-size:18px;width:290px;display:flex;justify-content:space-between}
.room-note{left:773px;top:390px;font-size:11px;font-style:italic;color:var(--green)}

/* about */
.about{top:1309px;height:394px}
.about .copy{left:93px;top:118px;width:501px;text-align:center;font-size:17px;font-style:italic;font-weight:300;color:var(--grey);line-height:21px}
.text-link{color:var(--navy);font-weight:600;font-size:21px}
.about .badge{left:802px;top:104px;width:200px;height:200px;border-radius:50%;background:var(--green)}
.about .badge-name{left:752px;top:316px;width:300px;text-align:center;font-size:22px;font-weight:600;color:var(--navy);letter-spacing:1px}

/* membership */
.membership{top:1703px;height:144px;background:var(--navy);color:var(--white)}
.membership p{right:531px;top:47px;width:600px;text-align:center;font-size:19px;line-height:24px}
.membership .btn-outline{left:712px;top:41px;width:273px;height:62px;font-size:29px;font-weight:600}

/* testimonials */
.testimonials{top:1847px;height:336px}
.testimonials .section-title{font-weight:600}
.avatar{left:722px;top:68px;width:106px;height:106px;background:linear-gradient(150deg,#9bc3d6,#d8b49a 55%,#6b7f8f)}
.quote-name{left:848px;top:72px;font-family:"Roboto",Arial,sans-serif;font-size:24px;font-weight:300;line-height:31px;color:var(--ink)}
.quote-role{left:848px;top:132px;font-size:15px;font-style:italic;font-weight:300;color:var(--green);line-height:18px}
.quote-text{left:726px;top:192px;width:300px;font-family:Arial,Helvetica,sans-serif;font-size:14px;line-height:18px;color:var(--ink)}
.pager{left:1157px;top:117px;display:flex;flex-direction:column;gap:11px}
.pager span{width:14px;height:14px;border-radius:50%;background:var(--dot)}

/* contact */
.contact{top:2183px;height:400px}
.contact h2{left:0;width:1200px;text-align:center;top:30px;font-size:36px;font-weight:400;color:#333}
.contact .small{left:0;width:1200px;text-align:center;top:70px;font-size:11px;line-height:14px;color:var(--grey)}
.field-label{font-size:15px;color:var(--ink)}
.field{border:1px solid #8a8a8a;border-radius:4px;font-size:10px;color:#a0a0a0;padding:3px 6px;font-family:"Open Sans",sans-serif}
.btn-send{left:530px;top:337px;width:141px;height:35px;background:var(--navy);color:var(--white);font-size:21px;font-weight:600;display:flex;align-items:center;justify-content:center}

/* footer */
.site-footer{top:2583px;height:267px;background:var(--footer);border-top:1px solid var(--rule)}
.site-footer .brand{left:442px;top:60px}
.site-footer .brand .mark{width:64px;height:64px}
.footer-nav{left:0;width:1200px;top:162px;display:flex;justify-content:center;gap:26px;font-size:17px;font-weight:700;letter-spacing:-.5px;color:var(--ink)}
.footer-social{left:0;width:1200px;top:200px;display:flex;justify-content:center;gap:10px;color:var(--navy)}
.footer-rule{left:345px;width:508px;top:250px;height:1px;background:var(--rule)}
.copyright{left:0;width:1200px;text-align:center;top:256px;font-size:7px;color:var(--grey)}
</style>
</head>
<body>

<div class="topbar">
  <div class="abs social">
    <svg width="20" height="18" viewBox="0 0 20 18" aria-label="Share"><path d="M2 16 C3 8 8 6 13 6 V2 L19 8 L13 14 V10 C8 10 5 11 2 16Z" fill="#fff"/></svg>
    <span class="dot-icon" aria-label="Social link"></span>
    <span class="dot-icon" aria-label="Social link"></span>
    <span class="dot-icon" aria-label="Social link"></span>
  </div>
  <a class="abs account" style="left:944px">Login</a>
  <a class="abs account" style="left:1045px">Registration</a>
</div>

<header class="site-header">
  <div class="abs brand">
    <span class="mark"></span>
    <div><div class="name">QUILLMONT</div><div class="tag">BOOKING ENGINE</div></div>
  </div>
  <nav class="abs main-nav">
    <span class="current">Home</span><span>Reservation</span><span>Rooms</span><span>About</span><span>Testimonials</span><span>Contact</span>
  </nav>
</header>

<section class="hero" role="img" aria-label="Soft-focus breakfast tray with apples and toast on white bed linen">
  <div class="abs rule" style="top:126px"></div>
  <p class="abs intro">Lorem ipsum dolor sit amet, consectetur adipiscing elit. Morbi auctor ipsum quis mauris tristique consectetur. Praesent vulputate vel lacus eget pretium. Lorem ipsum dolor sit amet, consectetur adipiscing elit. Praesent finibus porta nisi, sed scelerisque quam sodales nec. Sed sagittis, ex et dapibus lobortis, dui erat pretium massa, a cursus ipsum libero at eros. Nullam lectus ex, rutrum in tellus eget, viverra tristique leo. Class aptent taciti sociosqu ad litora torquent per conubia nostra, per inceptos himenaeos.</p>
  <div class="abs rule" style="top:332px"></div>
  <a class="abs btn-outline">Read More</a>
</section>

<section class="features">
  <div class="tile navy">
    <svg width="56" height="62" viewBox="0 0 56 62" aria-hidden="true"><rect x="1" y="1" width="54" height="60" rx="4" fill="#fff"/><rect x="8" y="8" width="40" height="11" fill="#004b82"/><g fill="#004b82"><rect x="8" y="25" width="8" height="7"/><rect x="20" y="25" width="8" height="7"/><rect x="32" y="25" width="8" height="7"/><rect x="8" y="36" width="8" height="7"/><rect x="20" y="36" width="8" height="7"/><rect x="32" y="36" width="8" height="7"/><rect x="8" y="47" width="8" height="7"/><rect x="20" y="47" width="8" height="7"/><rect x="32" y="47" width="8" height="7"/><rect x="42" y="25" width="6" height="29"/></g></svg>
    <h3>ESTIMATE</h3><p>Lorem ipsum dolor sit amet, consectetur adipiscing elit.</p>
  </div>
  <div class="tile green">
    <svg width="56" height="56" viewBox="0 0 56 56" aria-hidden="true"><circle cx="28" cy="28" r="24" fill="none" stroke="#fff" stroke-width="6"/><path d="M28 14 V30 H40" fill="none" stroke="#fff" stroke-width="5"/></svg>
    <h3>RESERVATION</h3><p>Lorem ipsum dolor sit amet, consectetur adipiscing elit.</p>
  </div>
  <div class="tile navy">
    <svg width="42" height="58" viewBox="0 0 42 58" aria-hidden="true"><path d="M21 2 C10 2 2 10 2 21 C2 35 21 56 21 56 C21 56 40 35 40 21 C40 10 32 2 21 2Z" fill="#fff"/><circle cx="21" cy="20" r="7" fill="#004b82"/></svg>
    <h3>OUR LOCATION</h3><p>Lorem ipsum dolor sit amet, consectetur adipiscing elit.</p>
  </div>
  <div class="tile green">
    <svg width="54" height="54" viewBox="0 0 54 54" aria-hidden="true"><path d="M12 3 L20 12 C21 14 20 16 18 18 L16 20 C19 27 26 34 34 38 L36 36 C38 34 40 33 42 34 L51 42 C52 44 51 46 49 48 C45 52 39 53 32 49 C20 43 11 34 5 22 C1 15 2 9 6 5 C8 3 10 2 12 3Z" fill="#fff"/></svg>
    <h3>CALL US</h3><p>Lorem ipsum dolor sit amet, consectetur adipiscing elit.</p>
  </div>
</section>

<section class="rooms">
  <h2 class="abs section-title" style="top:162px">ROOMS</h2>
  <p class="abs lede" style="top:206px">Lorem ipsum dolor sit amet, consectetur adipiscing elit. Duis malesuada, felis eu efficitur bibendum, sem arcu.</p>
  <div class="abs accent" style="left:268px;top:265px;width:116px"></div>
  <a class="abs arrow-btn" style="left:696px;top:204px" aria-label="Previous room"><svg width="14" height="22" viewBox="0 0 14 22"><path d="M11 2 L3 11 L11 20" fill="none" stroke="#fff" stroke-width="3"/></svg></a>
  <div class="abs room-card"><div class="room-photo" role="img" aria-label="Hotel room with an orange-covered bed and a city view window"></div></div>
  <a class="abs arrow-btn" style="left:1082px;top:204px" aria-label="Next room"><svg width="14" height="22" viewBox="0 0 14 22"><path d="M3 2 L11 11 L3 20" fill="none" stroke="#fff" stroke-width="3"/></svg></a>
  <div class="abs room-name"><span>Lorem ipsum dolor sit.</span><span>$99.99</span></div>
  <div class="abs room-note">Lorem ipsum dolor sit amet, consectetur adipiscing elit.</div>
</section>

<div class="abs divider" style="top:1309px"></div>

<section class="about">
  <h2 class="abs section-title" style="top:48px">ABOUT US</h2>
  <div class="abs accent" style="left:268px;top:98px;width:116px"></div>
  <p class="abs copy">Lorem ipsum dolor sit amet, consectetur adipiscing elit. Morbi auctor ipsum quis mauris tristique consectetur. Praesent vulputate vel lacus eget pretium. Lorem ipsum dolor sit amet, consectetur adipiscing elit. Praesent finibus porta nisi, sed scelerisque quam sodales nec. Sed sagittis, ex et dapibus lobortis, dui erat pretium massa, a cursus ipsum libero at eros. Nullam lectus ex, rutrum in tellus eget, viverra tristique leo. Class aptent taciti sociosqu ad litora torquent per conubia nostra, per inceptos himenaeos.</p>
  <a class="abs text-link" style="left:279px;top:340px">Read More</a>
  <div class="abs badge"></div>
  <div class="abs badge-name">QUILLMONT</div>
</section>

<section class="membership">
  <p class="abs">Lorem ipsum dolor sit amet, consectetur adipiscing elit.<br>Duis malesuada, felis eu efficitur bibendum, sem arcu.</p>
  <a class="abs btn-outline">Membership</a>
</section>

<section class="testimonials">
  <h2 class="abs section-title" style="top:110px">Testimonials</h2>
  <p class="abs lede" style="top:156px">Lorem ipsum dolor sit amet, consectetur adipiscing elit. Duis malesuada, felis eu efficitur bibendum, sem arcu.</p>
  <div class="abs accent" style="left:268px;top:212px;width:116px"></div>
  <div class="abs avatar" role="img" aria-label="Portrait of a smiling customer"></div>
  <div class="abs quote-name">Pellente Hab<br>Mortis Ot.</div>
  <div class="abs quote-role">Lorem ipsum dolor sit amet,<br>consectetur adipiscing elit.</div>
  <p class="abs quote-text">Vivamus scelerisque mi a vehicula maximus. Donec dapibus enim sed nibh ultricies, ut iaculis nisi venenatis. Vestibulum enim nibh, interdum sed sagittis a, bibendum non neque. Morbi at condimentum justo. Mauris facilisis lectus sed</p>
  <div class="abs pager"><span></span><span></span><span></span><span></span><span></span></div>
</section>

<div class="abs divider" style="top:2182px"></div>

<section class="contact">
  <h2 class="abs">CONTACT US</h2>
  <p class="abs small">Vivamus scelerisque mi a vehicula maximus. Donec dapibus enim sed nibh<br>ultricies, ut iaculis nisi venenatis. Vestibulum enim nibh, interdum sed sagittis</p>
  <div class="abs accent" style="left:500px;top:110px;width:198px;height:4px"></div>
  <label class="abs field-label" style="left:345px;top:148px">Name:</label>
  <div class="abs field" style="left:341px;top:168px;width:245px;height:21px">insert your name</div>
  <label class="abs field-label" style="left:345px;top:206px">Email:</label>
  <div class="abs field" style="left:341px;top:227px;width:245px;height:21px">insert your email address</div>
  <label class="abs field-label" style="left:345px;top:263px">Subject:</label>
  <div class="abs field" style="left:341px;top:285px;width:245px;height:21px">insert your subject</div>
  <label class="abs field-label" style="left:622px;top:146px">Message:</label>
  <div class="abs field" style="left:613px;top:166px;width:246px;height:138px">insert your message</div>
  <a class="abs btn-send">Send</a>
</section>

<footer class="site-footer">
  <div class="abs brand">
    <span class="mark"></span>
    <div><div class="name">QUILLMONT</div><div class="tag">BOOKING ENGINE</div></div>
  </div>
  <nav class="abs footer-nav"><span>HOME</span><span>RESERVATION</span><span>ROOMS</span><span>ABOUT</span><span>TESTIMONIALS</span><span>CONTACT</span></nav>
  <div class="abs footer-social">
    <svg width="20" height="18" viewBox="0 0 20 18" aria-label="Share"><path d="M2 16 C3 8 8 6 13 6 V2 L19 8 L13 14 V10 C8 10 5 11 2 16Z" fill="#004b82"/></svg>
    <span class="dot-icon" aria-label="Social link"></span>
    <span class="dot-icon" aria-label="Social link"></span>
    <span class="dot-icon" aria-label="Social link"></span>
  </div>
  <div class="abs footer-rule"></div>
  <div class="abs copyright">© Quillmont. All rights reserved.</div>
</footer>

</body>
</html>
```